Home Delivery Startup needs a web design!

Hello,
We're a start-up company in the final mile logistics industry. Our name is Brightwater Freight Collective. We partner with retailers throughout the USA and Canada and can perform the following services:
Home Delivery
Warehousing
Assembly
We like grey tones and an ability to incorporate our logo and it's colors throughout the site.
We pride ourselves as being a customizable logistics solution .
Our=comprehensive customer support and advanced technology systems make us distinguishable for every delivery solution.
Strategically located distribution centers throughout North America give us an advantage to get product to customers quickly, safely and conveniently, with consistent, efficient service.
Target Market(s)
Retailers in the US and Canada
Industry/Entity Type
Industry
Coding
Coded - Design and coding required
Number of Pages Required
5+ page

```html
<!DOCTYPE html>
<html lang="en">
<head>
<meta charset="utf-8">
<title>Brightwater Freight Collective</title>
<link href="https://fonts.googleapis.com/css2?family=Open+Sans:ital,wght@0,400;0,600;0,700;1,400&display=swap" rel="stylesheet">
<style>
  :root {
    --brand: #2c5a7e;
    --brand-dark: #2f5878;
    --heading: #2b5475;
    --text: #333a40;
    --muted: #6b7075;
    --footer: #32373d;
    --footer-bottom: #2b2f34;
    --footer-text: #c9cdd1;
    --footer-muted: #8f959b;
    --white: #ffffff;
    --rule: #dcdfe2;
  }
  * { box-sizing: border-box; margin: 0; padding: 0; }
  html, body { width: 1096px; height: 1200px; overflow: hidden; background: var(--white); }
  body { position: relative; font-family: "Open Sans", Arial, sans-serif; color: var(--text); }
  .abs { position: absolute; }

  /* Header */
  .site-header { position: absolute; left: 0; top: 0; width: 1096px; height: 69px; background: var(--white); }
  .brand { position: absolute; left: 90px; top: 10px; display: flex; align-items: center; gap: 9px; }
  .brand-dot { width: 40px; height: 40px; border-radius: 50%; background: var(--brand); }
  .brand-name { font-weight: 700; font-size: 15px; line-height: 17px; color: var(--brand); }
  .main-nav a { position: absolute; top: 31px; font-size: 9.5px; color: #3c4349; text-decoration: none; text-transform: uppercase; }
  .call { position: absolute; display: flex; align-items: center; gap: 10px; }
  .call-label { font-size: 13px; line-height: 16px; color: #8b9197; }
  .call-number { font-size: 15.5px; line-height: 18px; color: var(--brand); }

  /* Hero */
  .hero { position: absolute; left: 0; top: 69px; width: 1096px; height: 434px; overflow: hidden;
    background: linear-gradient(180deg, #4f86d0 0%, #7da6dc 45%, #4b5a6b 62%, #2a3340 72%, #2f5c86 88%, #285276 100%); }
  .hero-photo { position: absolute; inset: 0;
    background: linear-gradient(100deg, rgba(30,30,36,0.0) 0%, rgba(20,22,28,0.55) 20%, rgba(35,30,32,0.5) 55%, rgba(160,70,50,0.25) 75%, rgba(0,0,0,0) 100%); }
  .hero-title { position: absolute; left: 530px; top: 283px; width: 520px; font-weight: 700; font-size: 24px; line-height: 33px; color: var(--white); }
  .hero-arrows { position: absolute; left: 532px; top: 360px; display: flex; gap: 1px; }
  .arrow-btn { width: 23px; height: 23px; background: rgba(90,96,104,0.75); display: flex; align-items: center; justify-content: center; }

  /* Content */
  .section-title { position: absolute; top: 549px; font-weight: 700; font-size: 15px; color: var(--heading); text-transform: uppercase; }
  .news-photo { position: absolute; left: 90px; top: 593px; width: 313px; height: 173px;
    background: linear-gradient(180deg, #4f8fd6 0%, #a8c8ea 50%, #a55a3d 62%, #3d6e9a 80%, #9a9a98 100%); }
  .news-arrows { position: absolute; left: 350px; top: 738px; display: flex; gap: 1px; }
  .news-arrows .arrow-btn { width: 23px; height: 22px; background: rgba(80,84,90,0.8); }
  .news-title { position: absolute; left: 90px; top: 776px; font-size: 12.5px; color: #2c3237; }
  .news-date { position: absolute; left: 90px; top: 799px; font-size: 11.5px; color: var(--brand); }
  .body-text { font-size: 10.2px; line-height: 19.5px; color: var(--muted); }
  .news-body { position: absolute; left: 90px; top: 822px; width: 310px; line-height: 20.5px; }

  .service { position: absolute; top: 594px; width: 173px; }
  .service-photo { width: 173px; height: 124px; }
  .service-name { margin-top: 14px; font-weight: 700; font-size: 14px; color: var(--heading); }
  .service .body-text { margin-top: 4px; }
  .read-more { margin-top: 11px; width: 92px; height: 27px; background: var(--brand-dark); color: var(--white);
    font-weight: 700; font-size: 8.5px; display: flex; align-items: center; justify-content: center; gap: 4px; text-transform: uppercase; }

  .divider { position: absolute; left: 90px; top: 906px; width: 913px; height: 1px; background: var(--rule); }

  /* Footer */
  .site-footer { position: absolute; left: 0; top: 910px; width: 1096px; height: 242px; background: var(--footer); }
  .footer-title { position: absolute; top: 40px; font-weight: 700; font-size: 11px; color: var(--white); text-transform: uppercase; }
  .footer-links { position: absolute; top: 67px; list-style: none; }
  .footer-links li { font-size: 9.5px; line-height: 20.3px; color: var(--footer-text); text-transform: uppercase; }
  .quote { position: absolute; left: 131px; top: 80px; width: 232px; font-style: italic; font-size: 9.3px; line-height: 18.8px; color: var(--footer-text); }
  .quote-mark { position: absolute; font-size: 22px; color: var(--footer-muted); font-family: Georgia, serif; }
  .quote-author { position: absolute; left: 128px; top: 193px; font-size: 10.5px; color: var(--footer-muted); }
  .quote-author strong { font-weight: 700; color: #b7bcc1; font-size: 9.5px; }
  .social { position: absolute; top: 66px; width: 25px; height: 25px; border-radius: 50%; background: #62676d; }
  .site-footer .call-label { color: #aeb3b8; }
  .site-footer .call-number { color: var(--white); }

  .footer-bottom { position: absolute; left: 0; top: 1152px; width: 1096px; height: 48px; background: var(--footer-bottom);
    display: flex; align-items: center; justify-content: center; font-size: 9.5px; color: #a3a8ad; text-transform: uppercase; }
</style>
</head>
<body>

<header class="site-header">
  <div class="brand">
    <span class="brand-dot"></span>
    <div class="brand-name">Brightwater<br>Freight Collective</div>
  </div>
  <nav class="main-nav">
    <a style="left:341px">About Us</a>
    <a style="left:428px">Services</a>
    <a style="left:511px">Clients</a>
    <a style="left:588px">Testimonials</a>
    <a style="left:695px">Contact Us</a>
  </nav>
  <div class="call" style="left:848px; top:16px;">
    <svg width="37" height="37" viewBox="0 0 37 37" aria-hidden="true">
      <circle cx="18.5" cy="18.5" r="17" fill="none" stroke="#2c5a7e" stroke-width="1.6"/>
      <path d="M14 10 l4 0 l1 5 l-2.5 1.5 q1.5 4 5 6.5 l2 -2 l4.5 2 l-0.5 4 q-9 1 -13.5 -17 z" fill="none" stroke="#2c5a7e" stroke-width="1.6" stroke-linejoin="round"/>
    </svg>
    <div>
      <div class="call-label">Call Us :</div>
      <div class="call-number">( 3265 ) 418 907</div>
    </div>
  </div>
</header>

<section class="hero">
  <div class="hero-photo" role="img" aria-label="Container ship loaded with stacked cargo containers at sea"></div>
  <h1 class="hero-title">Strategically located distribution centers throughout North America</h1>
  <div class="hero-arrows">
    <span class="arrow-btn"><svg width="8" height="12" viewBox="0 0 8 12"><path d="M6 1 L1 6 L6 11" fill="none" stroke="#fff" stroke-width="1.2"/></svg></span>
    <span class="arrow-btn"><svg width="8" height="12" viewBox="0 0 8 12"><path d="M2 1 L7 6 L2 11" fill="none" stroke="#fff" stroke-width="1.2"/></svg></span>
  </div>
</section>

<h2 class="section-title" style="left:90px">Latest News</h2>
<h2 class="section-title" style="left:431px">Services</h2>

<div class="news-photo" role="img" aria-label="Port terminal with gantry crane and stacked shipping containers"></div>
<div class="news-arrows">
  <span class="arrow-btn"><svg width="8" height="12" viewBox="0 0 8 12"><path d="M6 1 L1 6 L6 11" fill="none" stroke="#fff" stroke-width="1.2"/></svg></span>
  <span class="arrow-btn"><svg width="8" height="12" viewBox="0 0 8 12"><path d="M2 1 L7 6 L2 11" fill="none" stroke="#fff" stroke-width="1.2"/></svg></span>
</div>
<h3 class="news-title">Es simplemente el texto de relleno de las</h3>
<p class="news-date">Posted on 27 November 2014</p>
<p class="body-text news-body">Es simplemente el texto de relleno de las imprentas y archivos de texto. Lorem Ipsum ha sido el texto de...</p>

<article class="service" style="left:434px">
  <div class="service-photo" role="img" aria-label="Courier handing a parcel to a customer at her door" style="background:linear-gradient(90deg,#d9d6d0 0%,#f1eee8 45%,#b08a68 70%,#5a4434 100%)"></div>
  <h3 class="service-name">Home Delivery</h3>
  <p class="body-text">Es simplemente el texto de relleno de las imprentas y archivos de texto ha sido el texto de...</p>
  <div class="read-more">Read More <span>&raquo;</span></div>
</article>
<article class="service" style="left:634px">
  <div class="service-photo" role="img" aria-label="Warehouse worker with boxes on a hand truck between shelves" style="background:linear-gradient(90deg,#7a5a3a 0%,#a07b52 30%,#3f5f9a 50%,#b28a5c 75%,#6e5238 100%)"></div>
  <h3 class="service-name">Warehousing</h3>
  <p class="body-text">Es simplemente el texto de relleno de las imprentas y archivos de texto ha sido el texto de...</p>
  <div class="read-more">Read More <span>&raquo;</span></div>
</article>
<article class="service" style="left:833px">
  <div class="service-photo" role="img" aria-label="Worker pulling a pallet jack with boxes across a warehouse floor" style="background:linear-gradient(135deg,#4f6a64 0%,#6f8a84 50%,#8c9ea0 75%,#c7a36e 100%)"></div>
  <h3 class="service-name">Assembly</h3>
  <p class="body-text">Es simplemente el texto de relleno de las imprentas y archivos de texto ha sido el texto de...</p>
  <div class="read-more">Read More <span>&raquo;</span></div>
</article>

<div class="divider"></div>

<footer class="site-footer">
  <h4 class="footer-title" style="left:111px">Testimonials</h4>
  <svg class="abs" style="left:350px; top:42px" width="20" height="9" viewBox="0 0 20 9" aria-hidden="true">
    <path d="M4 1 L1 4.5 L4 8" fill="none" stroke="#8f959b" stroke-width="1"/>
    <path d="M15 1 L18 4.5 L15 8" fill="none" stroke="#8f959b" stroke-width="1"/>
  </svg>
  <span class="quote-mark" style="left:108px; top:68px">&ldquo;</span>
  <p class="quote">Simply dummy text of the printing and typesetting industry. Lorem Ipsum has been the industry's standard dummy text ever since the 1500s, when an unknown printer took a galley of type and scrambled it to make a type specimen book...</p>
  <span class="quote-mark" style="left:359px; top:152px">&rdquo;</span>
  <p class="quote-author"><strong>MAREN HOLT</strong> Marketing Executive</p>

  <h4 class="footer-title" style="left:466px">Welcome</h4>
  <ul class="footer-links" style="left:466px">
    <li>&nbsp;Home</li><li>About Us</li><li>Services</li><li>Clients</li><li>Testimonials</li><li>Contact Us</li>
  </ul>

  <h4 class="footer-title" style="left:660px">Information</h4>
  <ul class="footer-links" style="left:660px">
    <li>Privacy Policy</li><li>Terms &amp; Conditions</li><li>Sitemap</li>
  </ul>

  <h4 class="footer-title" style="left:846px">Follow Us</h4>
  <span class="social" style="left:845px" aria-label="Social profile"></span>
  <span class="social" style="left:878px" aria-label="Social profile"></span>
  <span class="social" style="left:914px" aria-label="Social profile"></span>
  <span class="social" style="left:948px" aria-label="Social profile"></span>

  <div class="call" style="left:848px; top:126px;">
    <svg width="37" height="37" viewBox="0 0 37 37" aria-hidden="true">
      <circle cx="18.5" cy="18.5" r="17" fill="none" stroke="#c9cdd1" stroke-width="1.6"/>
      <path d="M14 10 l4 0 l1 5 l-2.5 1.5 q1.5 4 5 6.5 l2 -2 l4.5 2 l-0.5 4 q-9 1 -13.5 -17 z" fill="none" stroke="#c9cdd1" stroke-width="1.6" stroke-linejoin="round"/>
    </svg>
    <div>
      <div class="call-label">Call Us :</div>
      <div class="call-number">( 3265 ) 418 907</div>
    </div>
  </div>
</footer>

<div class="footer-bottom">&copy; 2015. Brightwater Freight Collective. All rights reserved.</div>

</body>
</html>
```